Food Safety 1-California workers only

3.25" by 4.5" Black and White Magazine Ad
This ad is to train California workers only.
Workers will be trained on: Food Safety, FSMA (Food Safety Modernization Act), using equipment safety, food processing production skills, worker safety, supervisory skills, communication skills.
"FREE TRAINING", The company does the training or Keystone Learning will provide the training.
Training grants range from $100,000 to $400,000.
Companies must be in business for profit.
Companies must train 200 employees or more.
This program is for California workers only.
Incumbent or new-hires are eligible.

Target Market(s)

California food processors, farms, food packaging, food processors, companies under FSMA, food safety, food production who need to train employees.

Industry/Entity Type

Food Production

Font styles to use
Serif
Sans Serif

Colors

Designer to choose colors to be used in the design.

Requirements
Must have
• This is a 3.25 inch by 4.5 inch magazine ad. It must be black and white. No color.
• The deliverable must be in basic PhotoShop. The ad does not need to include any graphics and be text only if needed. If you have a black and white graphic that will show well.
• Look at www.KLGFoodSafety..com
• Use the text from "MEALBOX-Photoshop-052018" file as your starting point.
Nice to have
• A black and white graphic about food. See www.KLGFoodSafety.com
Should not have
• No color.

```html
<!DOCTYPE html>
<html lang="en">
<head>
<meta charset="utf-8">
<title>Free Training – Keystone Learning</title>
<link href="https://fonts.googleapis.com/css2?family=Montserrat:wght@400;500;600;700&display=swap" rel="stylesheet">
<style>
:root{
  --ink:#0c0c0c;
  --paper:#ffffff;
  --backdrop:#d9d9d9;
  --roller:#a9a9ab;
  --figure-light:#d4d4d4;
  --figure-dark:#3a3a3a;
}
*{margin:0;padding:0;box-sizing:border-box}
html,body{width:946px;height:1200px;overflow:hidden;background:var(--backdrop)}
body{font-family:'Montserrat',sans-serif;color:var(--ink);position:relative}
.ad{position:absolute;left:49px;top:0;width:938px;height:1328px;background:var(--ink);transform:scale(0.9036);transform-origin:0 0}
.ad > *{position:absolute}
.top-strip{left:6px;top:13px;width:926px;height:47px;background:var(--paper)}
.header{left:6px;top:60px;width:926px;height:102px;display:flex;align-items:center;justify-content:center;color:var(--paper);font-weight:700;font-size:65px;letter-spacing:1px}
.body{left:6px;top:162px;width:926px;height:988px;background:var(--paper)}
.pitch{left:0;width:938px;text-align:center;font-weight:700;font-size:30px;line-height:40px}
.pitch-one{top:190px}
.pitch-or{top:286px;font-size:32px}
.pitch-two{top:342px;font-size:26px}
.quote{font-weight:700;font-size:72px;line-height:1}
.q1l{left:80px;top:208px}.q1r{left:810px;top:205px}
.q2l{left:44px;top:338px}.q2r{left:838px;top:335px}
.projector{left:263px;top:410px;width:631px;height:396px;background:linear-gradient(180deg,var(--roller) 0%,var(--roller) 12%,var(--ink) 16%,var(--ink) 100%);border-radius:28px 28px 30px 30px}
.screen-topics{left:309px;top:490px;padding-left:110px;list-style:none;color:var(--paper);font-weight:500;font-size:34px;line-height:41.7px}
.screen-topics li{position:relative}
.screen-topics li::before{content:"";position:absolute;left:-38px;top:12px;width:18px;height:18px;border-radius:50%;background:var(--paper);box-shadow:inset 0 0 0 5px var(--ink),inset 0 0 0 9px var(--paper)}
.presenter{left:18px;top:515px;width:190px;height:620px;border-radius:90px 90px 20px 20px;background:linear-gradient(180deg,var(--figure-light) 0%,var(--figure-dark) 30%,var(--figure-dark) 100%)}
.qualify-icon{left:233px;top:831px}
.qualify-title{left:313px;top:833px;font-weight:700;font-size:33px;letter-spacing:.5px}
.qualify-rule{left:672px;top:841px;width:260px;height:26px;background:var(--ink)}
.criteria{left:318px;top:894px;list-style:none;font-size:19.6px;line-height:33.4px;font-weight:400}
.criteria li{padding-left:44px;position:relative}
.criteria li::before{content:"✓";position:absolute;left:0;top:0;font-weight:600}
.footer{left:6px;top:1150px;width:926px;height:122px;color:var(--paper)}
.contact-badge{position:absolute;left:3px;top:38px;width:214px;height:44px;background:var(--paper);color:var(--ink);font-size:26px;font-weight:500;display:flex;align-items:center;justify-content:center}
.contact-list{position:absolute;list-style:none;font-size:17px;font-weight:500;line-height:34px}
.contact-list li{display:flex;align-items:center;gap:18px}
.contact-list svg{width:16px;height:16px;flex:none}
.person-list{left:268px;top:10px}
.office-list{left:553px;top:11px}
.office-list li{padding-left:34px}
.office-list li:first-child{padding-left:0}
.bottom-strip{left:6px;top:1272px;width:926px;height:46px;background:var(--paper);display:flex;align-items:center;justify-content:center;font-weight:700;font-size:22px;letter-spacing:8px}
</style>
</head>
<body>
<main class="ad">
  <div class="top-strip"></div>
  <h1 class="header">FREE TRAINING</h1>
  <div class="body"></div>

  <span class="quote q1l">“</span>
  <p class="pitch pitch-one">YOU DO THE TRAINING AND<br>THE STATE OF CALIFORNIA PAYS FOR IT.</p>
  <span class="quote q1r">”</span>
  <p class="pitch pitch-or">OR</p>
  <span class="quote q2l">“</span>
  <p class="pitch pitch-two">WE DO THE TRAINING AND THE STATE PAYS FOR IT.</p>
  <span class="quote q2r">”</span>

  <div class="projector" role="img" aria-label="Illustration of a pull-down projector screen on a stand"></div>
  <ul class="screen-topics">
    <li>FOOD SAFETY</li>
    <li>FSMA</li>
    <li>PRODUCTION SKILLS</li>
    <li>WORKER SAFETY</li>
  </ul>

  <div class="presenter" role="img" aria-label="Illustration of a presenter in a dark suit gesturing toward the training screen"></div>

  <svg class="qualify-icon" width="46" height="44" viewBox="0 0 46 44" aria-hidden="true">
    <rect x="2" y="2" width="30" height="40" rx="2" fill="none" stroke="#0c0c0c" stroke-width="4"/>
    <path d="M7 12l3 3 5-6M7 22l3 3 5-6M7 32l3 3 5-6" fill="none" stroke="#0c0c0c" stroke-width="2.5"/>
    <path d="M19 13h9M19 23h9M19 33h9" stroke="#0c0c0c" stroke-width="3"/>
    <rect x="37" y="8" width="6" height="26" fill="#0c0c0c"/>
    <path d="M37 34l3 6 3-6z" fill="#0c0c0c"/>
  </svg>
  <h2 class="qualify-title">HOW TO QUALIFY</h2>
  <div class="qualify-rule"></div>
  <ul class="criteria">
    <li>Train CALIFORNIA WORKERS ONLY”</li>
    <li>Trainees must earn $11/hour</li>
    <li>Full time worker only</li>
    <li>Employee must attend at least 8 hours of training</li>
    <li>You must train 200 or more employees</li>
    <li>Incumbent or new hire workers are eligiable</li>
    <li>Seasonal workers are eligiable</li>
  </ul>

  <footer class="footer">
    <div class="contact-badge">CONTACT US</div>
    <ul class="contact-list person-list">
      <li><svg viewBox="0 0 16 16" aria-hidden="true"><circle cx="8" cy="4.5" r="3.5" fill="#fff"/><path d="M1.5 15c0-4 3-6 6.5-6s6.5 2 6.5 6z" fill="#fff"/></svg>Daniel Moreno</li>
      <li><svg viewBox="0 0 16 16" aria-hidden="true"><path d="M3 1l3 3-1.5 2.5c1 2 3 4 5 5L12 10l3 3-2 2.5C7 15 1 9 .5 3z" fill="#fff"/></svg>(555) 014-2870</li>
      <li><svg viewBox="0 0 16 16" aria-hidden="true"><rect x="1" y="3" width="14" height="10" fill="none" stroke="#fff" stroke-width="1.6"/><path d="M1 3l7 6 7-6" fill="none" stroke="#fff" stroke-width="1.6"/></svg>Dan.Moreno@KLGCAL.com</li>
    </ul>
    <ul class="contact-list office-list">
      <li><svg viewBox="0 0 16 16" aria-hidden="true"><path d="M8 0a5.5 5.5 0 0 0-5.5 5.5C2.5 10 8 16 8 16s5.5-6 5.5-10.5A5.5 5.5 0 0 0 8 0z" fill="#fff"/><circle cx="8" cy="5.5" r="2" fill="#0c0c0c"/></svg>Keystone Learning Company, Inc</li>
      <li>1800 Harbor View Drive</li>
      <li>Suite 310&nbsp; Irvine, CA 92614</li>
    </ul>
  </footer>

  <div class="bottom-strip">WWW.KLGFOODSAFETY.COM</div>
</main>
</body>
</html>
```